No Credit Score TQ and KSV

I'm looking for a banner to display on emails as well as facebook. The facebook banner would need to be square and the other size is 728 x 90. We are a mortgage company that does mostly Military home loans. We would like to start out with just this banner, then do about 20 others once we find the right designer. I need something simple but that stands out. Our company website is www.harborpeakloans.com. The text for this will be ( Ask about our "No Credit Score" program for KSV and TQ)

```html
<!DOCTYPE html>
<html lang="en">
<head>
<meta charset="utf-8">
<title>Harbor Peak – No Credit Score Program</title>
<link rel="stylesheet" href="https://fonts.googleapis.com/css2?family=Lato:wght@400;700;900&display=swap">
<style>
  :root {
    --ink: #1f1f22;
    --white: #ffffff;
    --panel-green: rgba(46, 160, 88, 0.72);
    --cta-orange: #f26a21;
    --quote-grey: #b8b8b8;
    --meta-grey: #444448;
    --photo-sky: #b9c8c6;
    --photo-grass: #55a640;
    --photo-camo: #8f8a7c;
  }
  * { box-sizing: border-box; margin: 0; padding: 0; }
  html, body { width: 1200px; height: 1200px; overflow: hidden; background: var(--white); }
  body { font-family: "Lato", Arial, sans-serif; }

  .banner { position: relative; width: 1200px; height: 1200px; overflow: hidden; background: var(--white); }

  .hero-photo {
    position: absolute; left: 0; top: 0; width: 1200px; height: 1020px;
    background:
      radial-gradient(ellipse 420px 520px at 820px 620px, #e4e2dc 0%, rgba(228,226,220,0) 70%),
      radial-gradient(ellipse 560px 700px at 900px 520px, var(--photo-camo) 0%, rgba(143,138,124,0) 75%),
      linear-gradient(180deg, var(--photo-sky) 0%, #9fb3a8 45%, var(--photo-grass) 75%, #4f9d3a 100%);
  }

  .brand {
    position: absolute; left: 122px; top: 42px;
    display: flex; align-items: center; gap: 16px;
  }
  .brand-mark { width: 44px; height: 44px; background: var(--ink); }
  .brand-name {
    font-weight: 900; font-size: 52px; letter-spacing: 4px; color: var(--ink);
    text-transform: uppercase; line-height: 1;
  }

  .offer-panel {
    position: absolute; left: 123px; top: 255px; width: 447px; height: 411px;
    background: var(--panel-green);
    padding: 48px 0 0 48px; color: var(--white);
  }
  .offer-line { font-weight: 700; font-size: 31px; line-height: 1.2; }
  .offer-line.strong { font-size: 42px; line-height: 1.15; margin: 2px 0 6px; }
  .offer-line .programs { font-size: 46px; }

  .cta-button {
    position: absolute; left: 29px; top: 303px; width: 390px; height: 56px;
    background: var(--cta-orange); color: var(--white);
    font-weight: 700; font-size: 26px;
    display: flex; align-items: center; justify-content: center;
  }

  .testimonial { position: absolute; left: 0; top: 1020px; width: 1200px; height: 180px; }
  .quote-text {
    position: absolute; left: 0; top: 28px; width: 1200px; text-align: center;
    font-weight: 700; font-size: 23px; line-height: 35px; color: var(--ink);
  }
  .quote-line { display: block; white-space: nowrap; }
  .quote-line.first { padding-right: 6px; }
  .quote-line.second { padding-left: 30px; }
  .quote-mark {
    display: inline-block; width: 26px; height: 24px;
    vertical-align: 6px;
  }
  .quote-mark.open { margin-right: 4px; }
  .quote-mark.close { margin-left: 8px; }
  .quote-author {
    position: absolute; left: 640px; top: 102px; width: 160px; text-align: center;
    font-size: 19px; line-height: 24px; color: var(--meta-grey);
  }
  .quote-author .name { font-weight: 700; color: var(--ink); }
</style>
</head>
<body>
  <div class="banner">
    <div class="hero-photo" role="img" aria-label="Service member in camouflage uniform holding a small model house in cupped hands, green lawn behind"></div>

    <div class="brand">
      <span class="brand-mark"></span>
      <span class="brand-name">Harbor Peak</span>
    </div>

    <div class="offer-panel">
      <p class="offer-line">Ask about our</p>
      <p class="offer-line strong">"No Credit Score"</p>
      <p class="offer-line">program</p>
      <p class="offer-line">for <span class="programs">KSV and TQ</span></p>
      <div class="cta-button">Contact Us</div>
    </div>

    <div class="testimonial">
      <p class="quote-text">
        <span class="quote-line first"><svg class="quote-mark open" viewBox="0 0 26 24" aria-hidden="true"><path d="M2 23 L7 1 H13 L9 23 Z M14 23 L19 1 H25 L21 23 Z" fill="var(--quote-grey)"/></svg>I have never had such a great experience</span>
        <span class="quote-line second">with my TQ loan! Thank you Harbor Peak!!<svg class="quote-mark close" viewBox="0 0 26 24" aria-hidden="true"><path d="M5 1 H11 L7 23 H1 Z M17 1 H23 L19 23 H13 Z" fill="var(--quote-grey)"/></svg></span>
      </p>
      <div class="quote-author">
        <div class="name">-Marco</div>
        <div class="place">Ridgeview, CA</div>
      </div>
    </div>
  </div>
</body>
</html>
```